Vodka Bottle Label - Lune Vodka

I need a bottle label for a vodka I'd like to make called Lune Vodka.
I would like a label that looks elegant and fresh. I would like some mountains and colours to be red and white. Open to other colours being added but not too colourful. "Lune" means fresh, dawn in polish, i would like if mountains or something extra was added to the label too. I would like the Lune Vodka name not to be too small.
The vodka is made in australia and is 37%.

I would love to have a little bit of gold colour in the label!

I will provide the back label words when completing my decision.

i'd like to make it more simple and less european looking. More australian.

I saw a bottle like this and i did like the concept.

https://www.oakbarrelcellars.com.au/spirits/grey-vodka-range?srsltid=XqTz81mwkPLd04-hr-q7w93nfbzkgd_mR2yTpaMWxJeQ6vcbTnZsLpo

Target Market(s)

Vodka Drinkers

Industry/Entity Type

Alcohol

Colors
EB3D1F
EC4F4E
F09395
F8D3D4
FCEDEE

Requirements
Must have
• red and white colours incorporated, mountains or freshness on it.
Nice to have
• Fresh and clean look. Classy

```html
<!DOCTYPE html>
<html lang="en">
<head>
<meta charset="utf-8">
<title>Lune Vodka – Label Presentation</title>
<link rel="stylesheet" href="https://fonts.googleapis.com/css2?family=Montserrat:wght@800&family=Oswald:wght@500&family=Dancing+Script:wght@500&family=Roboto:wght@400&display=swap">
<style>
  :root {
    --red-deep: #EB3D1F;
    --red: #EC4F4E;
    --pink: #F09395;
    --blush: #F8D3D4;
    --mist: #FCEDEE;
    --navy: #14254A;
    --white: #FFFFFF;
    --stage-grey: #BDC6D0;
    --stage-light: #F2F4F6;
    --ink: #111111;
  }
  * { box-sizing: border-box; margin: 0; padding: 0; }
  html, body { width: 1200px; height: 897px; overflow: hidden; }
  body {
    position: relative;
    background: linear-gradient(90deg, var(--stage-grey), var(--stage-light) 55%, var(--stage-grey));
    font-family: "Roboto", Arial, sans-serif;
  }
  .showcase {
    position: absolute; left: 22px; top: 18px; width: 768px; height: 860px;
    background: linear-gradient(90deg, var(--stage-light) 0%, #E4E8EC 60%, var(--stage-grey) 100%);
    border-right: 2px solid #222;
  }
  .palette { position: absolute; left: 8px; top: 4px; display: flex; gap: 3px; background: var(--white); padding: 2px 3px 6px; }
  .swatch { width: 48px; display: flex; flex-direction: column; align-items: center; }
  .swatch span { display: block; width: 48px; height: 40px; }
  .swatch small { font-size: 6px; color: #777; margin-top: 2px; }

  .label {
    position: absolute;
    background: linear-gradient(90deg, var(--red) 0%, var(--pink) 50%, var(--red) 100%);
    display: flex; flex-direction: column; align-items: center; color: var(--white);
  }
  .label--front { left: 236px; top: 367px; width: 297px; height: 380px; border-radius: 0 0 50% 50% / 0 0 22px 22px; padding-top: 34px; }
  .label--flat { left: 31px; top: 43px; width: 303px; height: 370px; border-radius: 0 0 50% 50% / 0 0 18px 18px; padding-top: 28px; color: var(--navy); }

  .brand-name { font-family: "Montserrat", Arial, sans-serif; font-weight: 800; letter-spacing: 1px; line-height: 1; }
  .label--front .brand-name { font-size: 52px; }
  .label--flat .brand-name { font-size: 52px; }
  .mountains { border-radius: 4px; }
  .label--front .mountains { width: 226px; height: 98px; margin-top: 20px; background: linear-gradient(180deg, rgba(255,255,255,.75), rgba(255,255,255,.25)); }
  .label--flat .mountains { width: 226px; height: 98px; margin-top: 18px; background: linear-gradient(180deg, rgba(255,255,255,.75), rgba(255,255,255,.25)); }
  .subtitle { font-size: 16px; letter-spacing: 4px; margin-top: 18px; }
  .product { font-family: "Oswald", Arial, sans-serif; font-weight: 500; font-size: 32px; letter-spacing: 3px; line-height: 1.2; margin-top: 2px; }
  .origin { font-family: "Dancing Script", cursive; font-size: 12px; margin-top: 8px; }
  .stars { font-size: 18px; letter-spacing: 6px; margin-top: 8px; }
  .strength { font-size: 8px; letter-spacing: 2.5px; margin-top: 10px; }

  .panel { position: absolute; left: 812px; width: 364px; background: var(--white); }
  .panel--label { top: 20px; height: 464px; }
  .panel--mono { top: 500px; height: 224px; display: flex; flex-direction: column; align-items: center; color: var(--navy); padding-top: 44px; }
  .panel--mono .brand-name { font-size: 22px; }
  .panel--mono .mountains { width: 92px; height: 40px; margin-top: 6px; background: linear-gradient(180deg, var(--navy), rgba(20,37,74,.35)); }
  .panel--mono .subtitle { font-size: 7px; letter-spacing: 2px; margin-top: 7px; }
  .panel--mono .product { font-size: 12px; letter-spacing: 1.5px; }
  .panel--mono .origin { font-size: 5px; margin-top: 2px; }
  .panel--mono .stars { font-size: 7px; letter-spacing: 2px; margin-top: 2px; }
  .panel--mono .strength { font-size: 4px; letter-spacing: 1px; margin-top: 4px; }

  .note { position: absolute; left: 814px; top: 738px; width: 370px; font-family: Arial, sans-serif; font-style: italic; font-size: 19px; line-height: 1.25; color: var(--ink); }
  .note p + p { margin-top: 10px; }
</style>
</head>
<body>
  <section class="showcase">
    <div class="palette">
      <div class="swatch"><span style="background:var(--red-deep)"></span><small>EB3D1F</small></div>
      <div class="swatch"><span style="background:var(--red)"></span><small>EC4F4E</small></div>
      <div class="swatch"><span style="background:var(--pink)"></span><small>F09395</small></div>
      <div class="swatch"><span style="background:var(--blush)"></span><small>F8D3D4</small></div>
      <div class="swatch"><span style="background:var(--mist)"></span><small>FCEDEE</small></div>
    </div>
    <div class="label label--front">
      <div class="brand-name">LUNE</div>
      <div class="mountains" role="img" aria-label="White line drawing of mountain peaks"></div>
      <div class="subtitle">HIGH DESERT</div>
      <div class="product">VODKA</div>
      <div class="origin">Distilled from fine Queensland grapes</div>
      <div class="stars">★★★</div>
      <div class="strength">65% ALC/VOL - 750ML</div>
    </div>
  </section>

  <section class="panel panel--label">
    <div class="label label--flat">
      <div class="brand-name">LUNE</div>
      <div class="mountains" role="img" aria-label="White line drawing of mountain peaks"></div>
      <div class="subtitle">HIGH DESERT</div>
      <div class="product">VODKA</div>
      <div class="origin">Distilled from fine Queensland grapes</div>
      <div class="stars">★★★</div>
      <div class="strength">65% ALC/VOL - 750ML</div>
    </div>
  </section>

  <section class="panel panel--mono">
    <div class="brand-name">LUNE</div>
    <div class="mountains" role="img" aria-label="Navy line drawing of mountain peaks"></div>
    <div class="subtitle">HIGH DESERT</div>
    <div class="product">VODKA</div>
    <div class="origin">Distilled from fine Californian grapes</div>
    <div class="stars">★★★</div>
    <div class="strength">65% ALC/VOL - 750ML</div>
  </section>

  <div class="note">
    <p>If you would like some modifications, let me know, thank you.</p>
    <p>Si vous souhaitez quelques modifications, faites le moi savoir, merci.</p>
  </div>
</body>
</html>
```